Quellmar Aus Business card revamp

We are looking to revamp our business card design. We are hoping to change our colours to dark navey blue, gray, white and black but are open to keeping the same if a good design is submited. We are after somthing a bit differnt not just boring business card. I have attached a copy of our current card. We Want to keep the same logo design which i have attached a few to hopfully help you in this process. We are after a design that can be personalized to separate 4 people

Industry/Entity Type

Business

Colors
0455a3
ffffff
000000
cbcbcb

Requirements
Must have
• Quellmar Logo, address 3/41 Wattlebend Street, Kelvanby 4517, phone number, Name and position

```html
<!DOCTYPE html>
<html lang="en">
<head>
<meta charset="utf-8">
<title>Quellmar Aus — Business Card</title>
<link href="https://fonts.googleapis.com/css2?family=Montserrat:wght@800&family=Roboto:wght@400&display=swap" rel="stylesheet">
<style>
  :root {
    --stage: #484848;
    --card-dark: #000000;
    --card-light: #f4f4f4;
    --brand-blue: #2a7fd4;
    --ink: #1e1e1e;
    --fire-deep: #7a1a00;
    --fire-mid: #e0580c;
    --fire-bright: #ffb02e;
  }
  * { box-sizing: border-box; margin: 0; padding: 0; }
  html, body { width: 1200px; height: 1200px; overflow: hidden; }
  body { background: var(--stage); position: relative; font-family: "Roboto", Arial, sans-serif; }

  .card { position: absolute; width: 712px; height: 412px; border-radius: 16px; overflow: hidden; }
  .card--front { left: 166px; top: 152px; background: var(--card-light); }
  .card--back { left: 374px; top: 656px; background: var(--card-dark); }

  .card__band { position: absolute; left: 0; top: 0; width: 100%; height: 174px; background: var(--card-dark); }

  .brand { position: absolute; display: flex; flex-direction: column; align-items: center; }
  .brand__row { display: flex; align-items: center; gap: 14px; }
  .brand__dot { width: 26px; height: 26px; border-radius: 50%; background: var(--brand-blue); }
  .brand__name { font-family: "Montserrat", Arial, sans-serif; font-weight: 800; color: var(--brand-blue); line-height: 1; letter-spacing: -1px; }
  .brand__tagline { font-family: "Montserrat", Arial, sans-serif; font-weight: 800; color: var(--brand-blue); margin-top: 6px; letter-spacing: 0.5px; }

  .card--front .brand { left: 0; right: 0; top: 44px; }
  .card--front .brand__name { font-size: 54px; }
  .card--front .brand__tagline { font-size: 18px; }

  .card--back .brand { left: 0; right: 0; top: 74px; }
  .card--back .brand__name { font-size: 60px; }
  .card--back .brand__tagline { font-size: 20px; }

  .contact { position: absolute; right: 240px; top: 242px; list-style: none; }
  .contact__item { display: flex; align-items: center; justify-content: flex-end; gap: 14px; height: 30px; font-size: 19px; color: var(--ink); }
  .contact__icon { width: 16px; height: 16px; flex: none; }

  .divider { position: absolute; left: 497px; top: 210px; width: 2px; height: 172px; background: var(--ink); }

  .person { position: absolute; left: 527px; top: 270px; color: var(--ink); }
  .person__name { font-size: 25px; line-height: 1.1; }
  .person__title { font-size: 18px; margin-top: 4px; padding-left: 4px; }

  .flames { position: absolute; left: 0; right: 0; bottom: 0; height: 230px;
    background:
      radial-gradient(ellipse 28% 70% at 32% 100%, var(--fire-bright), transparent 70%),
      radial-gradient(ellipse 24% 60% at 72% 100%, var(--fire-bright), transparent 70%),
      radial-gradient(ellipse 70% 80% at 50% 100%, var(--fire-mid), transparent 75%),
      linear-gradient(to top, var(--fire-deep), transparent 80%);
  }
</style>
</head>
<body>

<section class="card card--front">
  <div class="card__band"></div>
  <div class="brand">
    <div class="brand__row">
      <span class="brand__dot"></span>
      <span class="brand__name">Quellmar</span>
    </div>
    <span class="brand__tagline">Passive Fire Protection</span>
  </div>

  <ul class="contact">
    <li class="contact__item">07 3418 6620
      <svg class="contact__icon" viewBox="0 0 16 16"><rect width="16" height="16" rx="2" fill="#2a7fd4"/><rect x="5" y="3" width="6" height="10" rx="1" fill="none" stroke="#fff" stroke-width="1.3"/></svg>
    </li>
    <li class="contact__item">+61 7 3418 6620
      <svg class="contact__icon" viewBox="0 0 16 16"><rect width="16" height="16" rx="2" fill="#2a7fd4"/><path d="M5 3.5l2 2-1 1.3c.7 1.4 1.8 2.5 3.2 3.2l1.3-1 2 2-1.2 1.5C8 12.2 3.8 8 3.5 4.7z" fill="#fff"/></svg>
    </li>
    <li class="contact__item">PO Box 248, Dunmore, QLD, 4519
      <svg class="contact__icon" viewBox="0 0 16 16"><rect width="16" height="16" rx="2" fill="#2a7fd4"/><path d="M8 3L3 7.5h1.5V12h2.5V9.5h2V12h2.5V7.5H13z" fill="#fff"/></svg>
    </li>
    <li class="contact__item">3/41 Wattlebend Street, Kelvanby 4517
      <svg class="contact__icon" viewBox="0 0 16 16"><rect width="16" height="16" rx="2" fill="#2a7fd4"/><path d="M8 2.5a3.5 3.5 0 0 0-3.5 3.5C4.5 9 8 13.5 8 13.5S11.5 9 11.5 6A3.5 3.5 0 0 0 8 2.5z" fill="#fff"/><circle cx="8" cy="6" r="1.3" fill="#2a7fd4"/></svg>
    </li>
  </ul>

  <div class="divider"></div>

  <div class="person">
    <div class="person__name">Your Name</div>
    <div class="person__title">Your Title</div>
  </div>
</section>

<section class="card card--back">
  <div class="brand">
    <div class="brand__row">
      <span class="brand__dot"></span>
      <span class="brand__name">Quellmar</span>
    </div>
    <span class="brand__tagline">Passive Fire Protection</span>
  </div>
  <div class="flames" role="img" aria-label="Photograph of orange flames rising from the bottom edge"></div>
</section>

</body>
</html>
```